Oil and Gas Construction Company Brochure Design

We're redesigning our company Brochure. The easiest part about this...the layout, content, photos, etc. will follow our newly redesigned website:

www.bravelquorn.com

Thank you very much and please contact me should you have any questions!

Target Market(s)

Engineers, management, and operators in the oil field services

Industry/Entity Type

Oil And Gas

Requirements
Must have
• The same layout as the website, the same content, the same photos (ask me if you need anymore photos or if the layout your chose needs more)
• Also, follow the same color scheme as the website. Follow the same feel/mood as the website. Follow the same text as the website.

```html
<!DOCTYPE html>
<html lang="en">
<head>
<meta charset="utf-8">
<title>Management – Bravelquorn Operations</title>
<link href="https://fonts.googleapis.com/css2?family=Arimo:ital,wght@0,400;0,500;1,400&display=swap" rel="stylesheet">
<style>
  :root {
    --page: #ffffff;
    --panel: #e3e0db;
    --panel-deep: #d2cec8;
    --accent: #7d1c22;
    --text: #2e2e2e;
    --rule: #3a3a3a;
  }
  html, body { margin: 0; padding: 0; overflow: hidden; }
  body { width: 927px; height: 1200px; background: var(--page); font-family: "Arimo", Helvetica, Arial, sans-serif; color: var(--text); }
  .page { position: relative; width: 927px; height: 1200px; overflow: hidden; }
  .panel {
    position: absolute; left: 43px; top: 43px; width: 841px; height: 1113px;
    background: linear-gradient(180deg, var(--panel-deep) 0%, var(--panel) 40%, var(--panel) 100%);
  }
  .section-title {
    position: absolute; left: 78px; top: 62px; margin: 0;
    font-size: 18px; font-weight: 500; letter-spacing: 7.5px; color: var(--accent);
  }
  .column { position: absolute; top: 103px; width: 248px; }
  .col-1 { left: 78px; }
  .col-2 { left: 343px; }
  .col-3 { left: 608px; }
  .bio + .bio { border-top: 1px solid var(--rule); margin-top: 11px; padding-top: 12px; }
  .bio-name { margin: 0; font-size: 13.6px; font-weight: 400; color: var(--accent); line-height: 17px; }
  .bio-role { margin: 3px 0 8px; font-size: 11.8px; font-style: italic; line-height: 15.2px; }
  .bio p { margin: 0 0 8px; font-size: 12.6px; line-height: 15.2px; }
  .bio p:last-child { margin-bottom: 0; }
  .folio {
    position: absolute; right: 43px; top: 1166px; font-size: 10.5px; letter-spacing: 2.2px;
  }
  .folio strong { font-weight: 500; margin-left: 12px; letter-spacing: 0; }
</style>
</head>
<body>
<div class="page">
  <div class="panel" role="img" aria-label="Faded photograph of a gas processing plant with storage tanks and piping"></div>
  <h1 class="section-title">MANAGEMENT</h1>

  <div class="column col-1">
    <section class="bio">
      <h2 class="bio-name">DARIO VELASQUIN</h2>
      <p class="bio-role">President &amp; Founder</p>
      <p>Mr. Velasquin has over 40 years of project development and management experience in the engineering and construction for the natural gas and petrochemical industries.</p>
      <p>He began his career in 1974 with Harwell Electric Co. Inc. In 1989 Mr. Velasquin served as General Manager for Harwell Electric Co. Inc. In 1996 he was promoted to Vice President of Operations for Harwell Industries Inc., where he was responsible for the operations of Harwell Electric Co. Inc., Harcon Inc., and Harwell Engineering and Construction Inc.</p>
      <p>His responsibilities included overseeing management personnel, safety, planning, forecasting, growth analysis, market assessments and maintaining the quality and profitability of all entities. From 2008 to 2010, Mr. Velasquin served as Chief Operating Officer for Harwell Industries, Inc. During his tenure, the Harwell companies experienced significant growth and expanded into numerous markets and opened two new regional offices.</p>
      <p>In 2000, Mr. Velasquin Co-founded and became Vice President of Keystar Gas Services, LLC, a contract gas treating company that was later sold to Redmesa Energy Services, L.P. (PXE: RMES) in 2003.</p>
    </section>
    <section class="bio">
      <h2 class="bio-name">TANNER ASHCOMBE, P.E.</h2>
      <p class="bio-role">Vice President of Business Development</p>
      <p>Mr. Ashcombe has over 13 years of experience in engineering, construction, operations, project management, and business development. Mr. Ashcombe’s engineering design experience includes: oil &amp; gas gathering and transmission, gas processing, gas conditioning, NGL &amp; condensate stabilization, structural design, large diameter pipelines, wastewater collection, conveyance and pump/lift station design, pipeline assessment, rehabilitation design, and water modeling.</p>
      <p>Prior to joining Bravelquorn, Mr. Ashcombe served as a Senior Engineer for Plainline Midstream (formerly Redmesa Energy). Previously, Mr. Ashcombe held various positions with Dunmore Engineering Solutions, Vantric, and Pellam Engineers.</p>
      <p>Mr. Ashcombe earned a Bachelor of Science in Civil Engineering from Llano State University and a Master of Science in Civil Engineering from Llano State University. In addition, Mr. Ashcombe is a Registered Professional Engineer in the State of Texas.</p>
    </section>
  </div>

  <div class="column col-2">
    <section class="bio">
      <h2 class="bio-name">RUBEN VELASQUIN</h2>
      <p class="bio-role">Vice President of Bravelquorn Constructors, Ltd.</p>
      <p>Mr. Velasquin has over 20 years of experience in providing heavy industrial electrical and general construction installations to the natural gas and petrochemical industries. He has managed and overseen major projects, such as cogeneration plants, compressor station installations, CO2 plant installations and relocations, grass roots amine plant installations, general maintenance projects and capital projects in the Oil &amp; Gas industry.</p>
      <p>Mr. Velasquin is directly responsible for all operational aspects of Bravelquorn Constructors, LTD, where he applies the importance of safety, quality, management, and cost control in all day to day activities.</p>
      <p>Prior to beginning his career in the Oil and Gas industry, Mr. Velasquin served in the United States Army as a Medical Specialist. During his service, Mr. Velasquin was deployed to Bosnia during Operation Joint Guard and Operation Joint Forge.</p>
      <p>Mr. Velasquin holds construction licenses in New Mexico and Oklahoma.</p>
    </section>
    <section class="bio">
      <h2 class="bio-name">MATEO RUELAS</h2>
      <p class="bio-role">Health, Safety, Environmental and Human Resources Director</p>
      <p>Mr. Ruelas joined Bravelquorn Operations in 2013 and brings over 12 years of experience in the Construction Industry, specializing in the refining, oil &amp; gas, nuclear, and mining sectors.</p>
      <p>Prior to joining Bravelquorn Mr. Ruelas served as Corporate HSE Manager for Harwell Industries and was responsible for managing field HSE representatives assigned to various projects. His duties also included providing HSE support for all projects that included implementation, communication and coordination of all environmental, health, and safety programs for the company.</p>
      <p>Mr. Ruelas earned a Certificate in Occupational Safety and Health Technology and an Associate of Science in Occupational Safety and Health Technology from Midvale College. In addition, Mr. Ruelas holds various certifications in the Construction and General Industries related to HSE including a double CSHO (Certified Safety and Health Official) in both the General and Construction Industries from Lone Plains Engineering Extension Service (LPEES).</p>
    </section>
  </div>

  <div class="column col-3">
    <section class="bio">
      <h2 class="bio-name">WALT KRENDLING</h2>
      <p class="bio-role">Vice President of Instrumentation &amp; Electrical</p>
      <p>Mr. Krendling serves as Vice President of Bravelquorn I&amp;E Ltd. He joined Bravelquorn in 2012 and brings 35 years of construction experience in the instrumentation, electrical and automation industry, specializing in the petrochemical, refining, gas processing, power and manufacturing sectors. He is directly responsible for all operational aspects of Bravelquorn I&amp;E, Ltd. with a heavy emphasis on safety, quality, management and cost control in all the day to day activities.</p>
      <p>Prior to joining Bravelquorn I&amp;E, Ltd., Mr. Krendling served in various roles during a 25 year career at Harwell Electric Co., Inc. most recently serving as Director of Electrical Services.</p>
      <p>Mr. Krendling holds various technical certifications and is a licensed Master Electrician in the State of Texas.</p>
    </section>
    <section class="bio">
      <h2 class="bio-name">JOEL CARRIZAL</h2>
      <p class="bio-role">Assistant Controller</p>
      <p>Mr. Carrizal serves as Assistant Controller of Bravelquorn Operations. He joined Bravelquorn in 2014 and has over 6 years’ experience in finance &amp; accounting. He is directly responsible for all accounting aspects of Bravelquorn Constructors, Ltd and Bravelquorn I&amp;E, Ltd including accounts receivable, accounts payable &amp; payroll.</p>
      <p>Prior to joining Bravelquorn, Mr. Carrizal served as Commercial Banking Officer and Credit Analyst at Prairie National Bank which specialized in commercial lending to the oil &amp; gas industry.</p>
      <p>Mr. Carrizal is also involved in various volunteer roles for a number of non-profit organizations. He has served as President of Bluebonnet House Children’s Advocacy Center, founding Board Member &amp; Treasurer of Young Professionals of Midvale, Chair for Leadership Midvale and Board Member for Midvale Community Fund.</p>
      <p>Mr. Carrizal earned a Master of Business Administration with a concentration in Finance from Llano State University.</p>
    </section>
  </div>

  <div class="folio">Bravelquorn Operations<strong>5</strong></div>
</div>
</body>
</html>
```